Business Card Design - Crisp & Clean

Looking for a new clean and crisp business card design. Design must incorporate our corporate colors (see attached style sheet). We're a pretty fun loving group who likes to keep it light while still portraying a professional image. Card should incorporate both our logo and our mascot (see attachment). Card should be double sided and should have room for our social media - Facebook, Linked In and Twitter on the back. Font selections do not have to match the style guide.

```html
<!DOCTYPE html>
<html lang="en">
<head>
<meta charset="utf-8">
<title>BrightPath Business Card</title>
<link rel="stylesheet" href="https://fonts.googleapis.com/css2?family=Oswald:wght@300;400;600;700&family=Yanone+Kaffeesatz:wght@300;400&family=Lato:wght@400&family=Tinos&display=swap">
<style>
  :root {
    --backdrop: #5d5d5f;
    --card-base: #e3e3e4;
    --card-shade: #cdcdce;
    --card-light: #ececed;
    --ink: #1b1b1b;
    --brand-gold: #f1b325;
    --link-blue: #3d6fc6;
    --phone-orange: #e8642a;
    --mascot-light: #ededed;
    --mascot-dark: #c9b8a4;
  }
  * { margin: 0; padding: 0; box-sizing: border-box; }
  html, body {
    width: 1200px;
    height: 900px;
    overflow: hidden;
    background: var(--backdrop);
  }
  .canvas {
    position: relative;
    width: 1200px;
    height: 900px;
  }
  .card {
    position: absolute;
    top: 300px;
    width: 520px;
    height: 300px;
    background: var(--card-base);
    overflow: hidden;
    box-shadow: 0 6px 18px rgba(0, 0, 0, 0.35);
  }
  .card--front { left: 50px; }
  .card--back { left: 630px; }
  .card__facets {
    position: absolute;
    inset: 0;
    width: 100%;
    height: 100%;
  }
  .mascot {
    position: absolute;
    left: 66px;
    top: 22px;
    width: 130px;
    height: 254px;
    border-radius: 10px;
    background: linear-gradient(180deg, var(--mascot-light) 0%, var(--mascot-dark) 100%);
  }
  .brand {
    position: absolute;
    left: 214px;
    top: 106px;
    display: flex;
    align-items: center;
    gap: 14px;
  }
  .brand__dot {
    width: 44px;
    height: 44px;
    border-radius: 50%;
    background: var(--brand-gold);
  }
  .brand__name {
    font-family: "Oswald", sans-serif;
    font-weight: 700;
    font-size: 40px;
    line-height: 1;
    color: var(--ink);
  }
  .contact {
    position: absolute;
    left: 0;
    width: 500px;
    top: 0;
    height: 100%;
    text-align: center;
  }
  .contact__name {
    position: absolute;
    left: 0; right: 0;
    top: 30px;
    font-family: "Oswald", sans-serif;
    font-weight: 700;
    font-size: 31px;
    line-height: 1;
    color: var(--ink);
    letter-spacing: 0.5px;
  }
  .contact__title {
    position: absolute;
    left: 0; right: 0;
    top: 72px;
    font-family: "Oswald", sans-serif;
    font-weight: 400;
    font-size: 21px;
    line-height: 1;
    color: var(--ink);
    letter-spacing: 0.8px;
  }
  .contact__company {
    position: absolute;
    left: 0; right: 0;
    top: 120px;
    font-family: "Yanone Kaffeesatz", sans-serif;
    font-weight: 400;
    font-size: 25px;
    line-height: 1;
    color: var(--brand-gold);
  }
  .contact__email {
    position: absolute;
    left: 0; right: 0;
    top: 164px;
    font-family: "Lato", sans-serif;
    font-size: 20px;
    line-height: 1;
    color: var(--link-blue);
    text-decoration: underline;
  }
  .contact__phone {
    position: absolute;
    left: 0; right: 0;
    top: 210px;
    display: flex;
    justify-content: center;
    align-items: center;
    gap: 8px;
    font-family: "Tinos", serif;
    font-size: 21px;
    line-height: 1;
    color: var(--phone-orange);
  }
  .contact__phone-icon { width: 20px; height: 20px; }
</style>
</head>
<body>
<main class="canvas">

  <section class="card card--front">
    <svg class="card__facets" viewBox="0 0 520 300" preserveAspectRatio="none" aria-hidden="true">
      <polygon points="0,0 455,0 0,135" fill="var(--card-shade)"/>
      <polygon points="455,0 520,0 520,300 500,300" fill="var(--card-light)"/>
    </svg>
    <div class="mascot" role="img" aria-label="Company mascot: cartoon scientist with white hair and glasses, arms crossed"></div>
    <div class="brand">
      <span class="brand__dot"></span>
      <span class="brand__name">BrightPath</span>
    </div>
  </section>

  <section class="card card--back">
    <svg class="card__facets" viewBox="0 0 520 300" preserveAspectRatio="none" aria-hidden="true">
      <polygon points="0,0 380,0 0,128" fill="var(--card-shade)"/>
      <polygon points="380,0 520,0 520,300 500,300" fill="var(--card-light)"/>
    </svg>
    <div class="contact">
      <h1 class="contact__name">MAYA COLLINS</h1>
      <p class="contact__title">Marketing Wizard</p>
      <p class="contact__company">BrightPath Processing Solutions</p>
      <p class="contact__email">maya@brightpath.com</p>
      <p class="contact__phone">
        <svg class="contact__phone-icon" viewBox="0 0 24 24" aria-hidden="true">
          <path d="M6.6 10.8a15.1 15.1 0 0 0 6.6 6.6l2.2-2.2a1 1 0 0 1 1-.25 11.4 11.4 0 0 0 3.6.57 1 1 0 0 1 1 1V20a1 1 0 0 1-1 1A17 17 0 0 1 3 4a1 1 0 0 1 1-1h3.5a1 1 0 0 1 1 1c0 1.25.2 2.45.57 3.6a1 1 0 0 1-.25 1z" fill="var(--phone-orange)"/>
        </svg>
        <span>555-014-2288</span>
      </p>
    </div>
  </section>

</main>
</body>
</html>
```